Amazon Fly/Cruise Expedition Cruise Package.

Task Description
I am wanting to create a double sided A4 colour flyer (Finished size: 297 x 210mm) for a Fly/Cruise package from Australia to the Amazon.
The idea is that I would like the art work or design work done for the flyer that I can then send to a printer to do the printing of these flyers.

My business is a retail cruise travel agent that specializes in selling all-inclusive packages on luxury expedition ships and in this case I intend to promote this cruise to people that are interested in wildlife and also bird watching.

This link will show you the full brochure from the Tour Operator that we will be using to give you more information on them and the cruise we are travelling on.
https://www.orvatrips.com/expedition/amazon-voyage#overview
This is an American company and basically I am giving you there brochure to give you more information.

I do all the costing's from Australia and ask you ignore the costing's etc. in their brochure, it will however give you more information to work with.

I will also attach my logo so this can be included and a copy of the draft itinerary that I see as being the highlights however I am aware that we are limited on space and we need to get the key issues across and also as the trip is being marketed to bird watchers and wildlife enthusiasts then some good pictures of both the boat and a few good birds ones and let’s say a bird called a ????? and maybe a monkey.

We also need to show the costing's and what's included in the package.

And of course a call to action
All bookings and enquiries call Derek

1-300-419-873
WaveHarbor Pty Ltd
derek@waveharbor.com.au
PO Box 817
Kelton NSW 2031
Australia.

Target Market(s)

Travellers that are interested in Birds/Animals and Expedition cruising.

Colors

Designer to choose colors to be used in the design.

Requirements
Must have
• Easy to read
• Colour full
• 2 birds pics
• 1 photo of the boat
• waveharbor logo
Nice to have
• a crisp clean look and a professional appearance

```html
<!DOCTYPE html>
<html lang="en">
<head>
<meta charset="utf-8">
<title>Explore the Peruvian Amazon – WaveHarbor Flyer</title>
<link href="https://fonts.googleapis.com/css2?family=Lexend:wght@300;400;500&family=Open+Sans:wght@400;600&display=swap" rel="stylesheet">
<style>
:root{
  --green:#2db673;
  --green-dark:#1f9a5c;
  --navy:#1d3a8a;
  --ink:#1a1a1a;
  --text:#333;
  --paper:#fff;
  --backdrop:#f0f0f0;
}
*{margin:0;padding:0;box-sizing:border-box}
html,body{width:1200px;height:1200px;overflow:hidden;background:var(--backdrop)}
body{font-family:"Open Sans",Arial,sans-serif;color:var(--text)}
.stage{position:absolute;left:0;top:0;width:1500px;height:1500px;transform:scale(.8);transform-origin:0 0}
.sheet{position:absolute;background:var(--paper);overflow:hidden}
.sheet--outside{left:88px;top:80px;width:942px;height:665px}
.sheet--inside{left:470px;top:773px;width:942px;height:667px}
.abs{position:absolute}
.photo{position:absolute}
.display{font-family:"Lexend",Arial,sans-serif;font-weight:400}
.brand{font-family:"Lexend",Arial,sans-serif;font-weight:500;color:var(--navy);font-size:15px;display:flex;align-items:center;gap:6px;letter-spacing:.3px}
.brand__dot{width:14px;height:14px;border-radius:50%;background:var(--navy)}

/* outside – left panel */
.ship-info{left:0;top:242px;width:315px;height:308px;background:var(--green);color:#fff;padding:14px 18px}
.ship-info h2{font-size:29px;font-weight:400;margin-bottom:8px}
.ship-info p{font-size:9.6px;line-height:13.4px;margin-bottom:12px}

/* outside – middle panel */
.intro{left:330px;top:93px;width:280px;font-size:11.5px;line-height:12.5px;color:#222}
.contact-list{left:340px;top:508px;list-style:none}
.contact-list li{display:flex;align-items:center;gap:8px;font-size:9px;height:38.5px;color:#222}
.contact-list svg{width:17px;height:17px;flex:none}
.square-grid{left:563px;top:503px;display:grid;grid-template-columns:repeat(3,14px);gap:10.5px 4px}
.square-grid span{width:14px;height:14px;background:var(--green)}

/* outside – cover */
.cover-title{left:640px;top:108px;font-size:36px;line-height:48px;color:var(--ink)}
.cover-title em{font-style:normal;color:var(--green)}
.tagline{left:630px;top:276px;width:312px;height:31px;background:linear-gradient(90deg,var(--navy),var(--green) 70%);color:#fff;font-family:"Lexend",Arial,sans-serif;font-size:13.5px;font-weight:300;display:flex;align-items:center;padding-left:13px}

/* inside */
.highlights{left:14px;top:160px;width:292px;list-style:none}
.highlights li{position:relative;padding-left:31px;font-size:10px;line-height:18px;margin-bottom:8px;text-align:justify}
.highlights li::before{content:"";position:absolute;left:0;top:5px;width:15px;height:13px;background:var(--green)}
.col-head{top:0;height:49px;display:flex;align-items:center;color:#fff}
.col-head--itinerary{left:315px;width:315px;background:#000;padding-left:13px;font-size:20px;letter-spacing:.5px}
.col-head--call{left:630px;width:312px;background:var(--green);padding-left:10px;flex-direction:column;align-items:flex-start;justify-content:center}
.col-head--call .call-line{font-size:18px;display:flex;gap:14px;align-items:baseline}
.col-head--call .call-line b{font-weight:400;font-size:21px;color:#111}
.col-head--call small{font-family:"Open Sans",Arial,sans-serif;font-size:7.5px;letter-spacing:.3px}
.day{position:absolute;border-left:3px solid var(--green);padding-left:11px;width:290px}
.day h3{font-family:"Lexend",Arial,sans-serif;font-weight:400;font-size:20px;color:var(--green);line-height:22px;margin-bottom:2px}
.day p{font-size:8.6px;line-height:12.3px;color:#222}
.arrival{left:328px;top:53px;width:290px;display:flex;gap:12px;font-size:8.6px;line-height:12.3px;color:#222}
.arrival span{width:15px;height:13px;background:var(--green);flex:none;margin-top:2px}
.divider{position:absolute;top:0;width:1px;height:100%;background:#e5e5e5}
</style>
</head>
<body>
<div class="stage">

  <!-- outside of the flyer -->
  <section class="sheet sheet--outside">
    <div class="photo" role="img" aria-label="Photo of the Marisol riverboat cruising on the Amazon" style="left:0;top:0;width:315px;height:242px;background:linear-gradient(180deg,#3d8fd6 0%,#8cc3ec 55%,#c8a57c 80%,#9b7a58 100%)"></div>
    <div class="abs ship-info">
      <h2 class="display">THE MARISOL</h2>
      <p>Travel aboard the Marisol, a luxurious vessel we have chartered for your adventure, which blends stylish design and modern comforts. Classic touches include magnificent floor-to-ceiling windows and — for those on the Upper Deck — private balconies. A ship staff and crew of 25, including a cruise director and local naturalist guides, are joined by an Orva Expedition Leader, Martin and Derek to ensure an unprecedented level of service. All 19 spacious suites are air-conditioned and feature en-suite bathrooms, a desk and ample closet space.</p>
      <p>We will be travelling in the High Water season this will allow us to go deeper into the Amazon Basin and further into the forest on our excursion boats we can also go into smaller tributaries- we will I hope see more wildlife and Birds that shun the main course of the river.</p>
    </div>
    <div class="photo" role="img" aria-label="Photo of a blue tanager perched among leaves" style="left:0;top:560px;width:126px;height:105px;background:linear-gradient(135deg,#4f7d3a,#2f8fbf 55%,#b8462e)"></div>
    <div class="photo" role="img" aria-label="Photo of a scarlet macaw in the rainforest" style="left:138px;top:560px;width:177px;height:105px;background:linear-gradient(135deg,#6a8f3a,#d23a1f 50%,#e2a52a 70%,#5d7f33)"></div>

    <p class="abs intro">WaveHarbor is a retail cruise travel agency that specializes in all-inclusive packages on luxury expedition ships &amp; travels</p>
    <div class="abs brand" style="left:332px;top:154px;color:#555"><span class="brand__dot" style="background:#555"></span>WAVEHARBOR</div>

    <ul class="abs contact-list">
      <li><svg viewBox="0 0 20 20"><circle cx="10" cy="10" r="10" fill="#2db673"/><path d="M7 5.5l2 2.2-1 1.4a6 6 0 0 0 3 3l1.4-1 2.2 2-1.2 1.6C9.5 14.5 6 11 5.4 6.7z" fill="#fff"/></svg>1-300-419-873</li>
      <li><svg viewBox="0 0 20 20"><circle cx="10" cy="10" r="10" fill="#2db673"/><rect x="5" y="6.5" width="10" height="7" fill="#fff"/><path d="M5 6.5l5 4 5-4" stroke="#2db673" fill="none"/></svg>derek@waveharbor.com.au</li>
      <li><svg viewBox="0 0 20 20"><circle cx="10" cy="10" r="10" fill="#2db673"/><path d="M10 4a3.6 3.6 0 0 0-3.6 3.6C6.4 10.5 10 15 10 15s3.6-4.5 3.6-7.4A3.6 3.6 0 0 0 10 4z" fill="#fff"/><circle cx="10" cy="7.6" r="1.3" fill="#2db673"/></svg>&nbsp;Kelton NSW 2031, Australia.</li>
      <li><svg viewBox="0 0 20 20"><circle cx="10" cy="10" r="10" fill="#2db673"/><circle cx="10" cy="10" r="5" fill="none" stroke="#fff" stroke-width="1.3"/><path d="M5 10h10M10 5c-2.5 3-2.5 7 0 10M10 5c2.5 3 2.5 7 0 10" stroke="#fff" fill="none" stroke-width="1"/></svg>waveharbor.com.au</li>
    </ul>
    <div class="abs square-grid">
      <span></span><span></span><span></span><span></span><span></span><span></span>
      <span></span><span></span><span></span><span></span><span></span><span></span>
      <span></span><span></span><span></span><span></span><span></span><span></span>
    </div>

    <div class="abs brand" style="left:643px;top:24px"><span class="brand__dot"></span>WAVEHARBOR</div>
    <h1 class="abs display cover-title">EXPLORE<br><em>THE PERUVIAN<br>AMAZON</em></h1>
    <div class="abs tagline">10 DAYS OF BREATH TAKING EXPEDITION</div>
    <div class="photo" role="img" aria-label="Photo of travellers in an excursion skiff among floating river plants and jungle" style="left:630px;top:307px;width:312px;height:358px;background:linear-gradient(180deg,#5d9ad6 0%,#a6c8e8 25%,#3d6b2e 45%,#5a9a3a 70%,#4f8c31 100%)"></div>
  </section>

  <!-- inside of the flyer -->
  <section class="sheet sheet--inside">
    <div class="photo" role="img" aria-label="Photo of the Marisol riverboat on a wide river" style="left:0;top:0;width:315px;height:137px;background:linear-gradient(180deg,#1d3a8a 0,#2db673 6px,#6ea4d8 6px,#b8d3ea 55%,#5c7a4a 75%,#9aa7b0 100%)"></div>
    <ul class="abs highlights">
      <li>Explore the Peruvian Amazon rainforest and its tributaries, experience wildlife as you voyage deep into the amazon river onboard the Marisol, a luxurious vessel that combines a blend of stylish design and modern confort.</li>
      <li style="text-align:left">Visit local communities and experience a range of cultural diversity, explore villages along the amazon river with a chance to learn about the lives of the people who live there, how they live, learn and grow.</li>
      <li style="text-align:left">Go fishing in grand style, find gray river dolphins, try your hand at piranha fishing in Ubas lake and find other fishing experiences. Also find birds like The Hyacinth Macaw, Blue Fronted Amazon Scarlet Macaws, Spectacled Owl, Plum Throated Cotinga, Crimson Topaz, Oropendolas and the Amazon Kingfisher.</li>
      <li style="text-align:left">Enjoy stargazing and storytelling with our guides while cruising slowly on the Amazon river, enjoy nighttime boat excursions for a chance to find caimans, common potos, frogs and other nocturnal wildlife.</li>
      <li style="text-align:left">Experience multiple daily excursions to see wildlife, explore the Pacay-samiria reserve, home to 450 bird species, 102 species of mammals, over 130 species of reptiles and amphibians and countless plants. Find Giant River Otters, Toucans, Macaws, Black Caimans, Capybaras, Pink River Dolphins, Piranhas and Jaguars.</li>
    </ul>

    <div class="divider" style="left:315px"></div>
    <div class="divider" style="left:630px"></div>

    <div class="abs col-head col-head--itinerary display">DAILY ITINERARY</div>
    <div class="abs arrival"><span></span>Fly from Australia to Lima Transfer from the airport to the Riverside Hotel Lima</div>

    <div class="day" style="left:335px;top:85px"><h3>DAY 1</h3><p>Tour the historic district of Lima. Visit the cathedral, where Francisco Pizarro is entombed, the Plaza de Armas, the monastery and vast catacombs of the Iglesia de San Francisco before visiting Casa Aliaga . Afterwards, we tour the ruins built by a Pre-Incan indigenous coastal civilization...</p></div>
    <div class="day" style="left:335px;top:192px"><h3>DAY 2</h3><p>Today we begin with a visit to the vibrant Indian Market where crafters display a wide variety of handmade items, jewelry, and art. We have lunch at a local restaurant and explore the surrounding shops before returning to the hotel to refresh before a late afternoon visit to the Larco Herrera Museum. We return to the hotel this evening and prepare for the next mornings' flight to Iquitos from Lima</p></div>
    <div class="day" style="left:335px;top:322px"><h3>DAY 3</h3><p>Fly over the Andes to Iquitos. Visit the Manatee Rescue Center, where biologists and volunteers care for endangered Amazon manatees that conservation authorities have rescued. Learn about efforts to help these endearing mammals. Board the elegant riverboat, Marisol, home for seven nights.</p></div>
    <div class="day" style="left:335px;top:418px"><h3>DAY 4</h3><p>We awake this morning on the Amazon River, seeing some of the ever-changing panorama of jungle life as the Amazon River cruise ship continues upriver. Small villages dot the shoreline, and channels weaving through island mazes provide close-up views of a variety of birds.Later we take an excursion into the surrounding rainforest in search of giant water lilies and elusive wildlife such as monkeys and sloths.</p></div>
    <div class="day" style="left:335px;top:544px"><h3>DAY 5</h3><p>After a peaceful breakfast along the black-water Sapote Creek, we explore a small tributary of the Ucayali aboard excursion boats. Look for animals including primates, sloths and an enormous variety of birds. Our Amazon Voyage adventure continues upriver to the Pacaya-Samiria Reserve. We enjoy a nighttime boat excursion for a chance to find caimans, capybaras, common potoos, frogs and other nocturnal wildlife.</p></div>

    <div class="abs col-head col-head--call display">
      <div class="call-line">CALL DEREK <b>1-300-419-873</b></div>
      <small>FOR BOOKINGS &amp; ENQUIRIES</small>
    </div>
    <div class="day" style="left:643px;top:57px"><h3>DAY 6</h3><p>Spend the day exploring this flooded realm, seeing wading birds such as herons, wattled jacanas and horned screamers. Venturing deep into the rainforest, tour an igapo (seasonally flooded forest), where plant life is very different from what we see along the main course of our Amazon cruise. A delicious lunch energizes us for afternoon excursions with our expert naturalists, where we may find scarlet macaws, hoatzins, black-collared hawks and red howler monkeys.</p></div>
    <div class="day" style="left:643px;top:190px"><h3>DAY 7</h3><p>After an early breakfast, we board excursion boats for access even further into the heart of these vast wetlands. As our Amazon Voyage adventure cruises the narrow waterways, we'll find birds such as canary-winged parakeets and spectacular blue-and-gold and scarlet macaws. Enjoy an al fresco lunch and time to relax before our afternoon excursion.</p></div>
    <div class="day" style="left:643px;top:307px"><h3>DAY 8</h3><p>Head back downriver, with a morning wildlife or other activity. Visit a village along the river, with the chance to learn about the lives of the "Ribereño" people who live there. Aboard the ship, learn to make traditional Peruvian dishes or enjoying an enriching lecture. After dark, go out in excursion boats to listen to the sounds of the rainforest and look for nocturnal wildlife.</p></div>
    <div class="day" style="left:643px;top:424px"><h3>DAY 9</h3><p>Wake up early for a morning birdwatching excursion along the Yarapa River. After breakfast, try your hand at piranha fishing in Ubos Lake. Piranha are very common in the slower-moving water. Once back aboard your luxury Amazon River cruise ship, we enjoy a farewell dinner.</p></div>
    <div class="day" style="left:643px;top:529px"><h3>DAY 10</h3><p>On an early morning excursion to Mariposa Rescue Center, see two- and three-toed sloth, red uakari and even a jaguar which have been rescued. Upon arrival back in Lima late this afternoon, dayrooms are provided until time to connect with independent overnight flights home. we fly from Iquitos to Lima where we connect with our flight back to Australia and arrive back in Sydney on the 27th April or you may wish to extend your trip.</p></div>
  </section>

</div>
</body>
</html>
```